Infographic to Present Investment Concept At A Glance

This infographic is designed to present the concept of KIT: Keep It Tangible as an investment strategy.
The concept of KIT is this: when investing your own money you are careful. You don't recklessly gamble your money and you tend to invest in understandable, local businesses or individuals that you know, to enrich your community. (See attached files).
For decades Finance professors taught to use OPM: Other People's Money to invest in Wall Street and global, complex investments that require a professional to manage. This system failed in 2008.
The concept of KIT is central to Clearwater Investing. This graphic is a centerpiece for presentations and the website.

It should be simple and understandable.

Elements to include in this graphic:
1- The logo and the Clearwater Investing name
2- The elements of KIT- Keep It Tangible (See attached files) stacked above OPM- Other People's Money so that the graphic can include or exclude OPM.
3- Earth tones emphasizing green tones
Updates

Hello everyone, We are now 2 days into the contest and no designs have been submitted. If you have questions, let me know. The deadline will not be extended for the project. I'll hope to see some designs soon.

Target Market(s)

Investors, Non-profits, website visitors, press organizations, presentation attendees

Industry/Entity Type

Investment

Font styles to use
Sans Serif

Requirements
Must have
• Logo
• Organization Name: "Clearwater Investing"
• The content from attachment: Kit vs OPM (Words)
• The content from Why Clearwater Investing in smaller letters
• The ability to crop the graphic to exclude OPM portion or include it separately
• An image that scrolls down
Nice to have
• Leaf, branch or root images
• Be creative with icons and elements

```html
<!DOCTYPE html>
<html lang="en">
<head>
<meta charset="utf-8">
<title>Clearwater Investing – KIT vs OPM</title>
<link href="https://fonts.googleapis.com/css2?family=Oswald:wght@500;600&family=Quicksand:wght@500;700&display=swap" rel="stylesheet">
<style>
  :root {
    --canvas: #ffffff;
    --field: #50ff5a;
    --band-dark: #3f9b45;
    --band-light: #5fc763;
    --header: #ffffff;
    --ink: #2a3a33;
    --ink-soft: #4a5d52;
    --label: #6b7f70;
    --accent: #f4f76a;
    --brand: #22394a;
    --brand-dot: #3fb24a;
    --tree: #3e9a47;
    --tree-deep: #2f7a38;
    --icon: #e6f56a;
  }
  * { box-sizing: border-box; margin: 0; padding: 0; }
  html, body { width: 1200px; height: 1000px; overflow: hidden; background: var(--canvas); }
  body { position: relative; font-family: "Quicksand", sans-serif; color: var(--ink); }

  .panel { position: absolute; top: 0; width: 572px; height: 1000px; background: var(--field); overflow: hidden; }
  .panel--compare { left: 0; }
  .panel--solo { left: 628px; }

  .top-band { position: absolute; left: 0; top: 0; width: 100%; height: 38px;
    background: linear-gradient(90deg, var(--band-dark), var(--band-light) 50%, var(--band-dark)); }
  .header { position: absolute; left: 0; top: 38px; width: 100%; height: 107px; background: var(--header); }
  .header-notch { position: absolute; left: 272px; top: 144px; width: 0; height: 0;
    border-left: 14px solid transparent; border-right: 14px solid transparent; border-top: 16px solid var(--header); }
  .brand { position: absolute; left: 0; top: 14px; width: 100%; display: flex; justify-content: center; align-items: center; gap: 10px; }
  .brand-dot { width: 34px; height: 34px; border-radius: 50%; background: var(--brand-dot); }
  .brand-name { font-family: "Quicksand", sans-serif; font-weight: 700; font-size: 27px; line-height: 26px; color: var(--brand); }
  .tagline { position: absolute; left: 0; top: 82px; width: 100%; text-align: center; font-weight: 700; font-size: 12px; color: var(--ink); }

  .why-title { position: absolute; left: 0; top: 204px; width: 100%; display: flex; justify-content: center; align-items: center; gap: 10px; }
  .why-title h2 { font-family: "Oswald", sans-serif; font-weight: 600; font-size: 21px; color: var(--accent); letter-spacing: 0.3px; }
  .divider { position: absolute; left: 266px; width: 40px; height: 12px; }
  .why-copy { position: absolute; left: 30px; top: 263px; width: 512px; text-align: center; font-size: 9.6px; line-height: 13.6px; color: var(--ink); font-weight: 500; }
  .why-copy strong { font-weight: 700; }
  .why-copy .goal { color: var(--accent); font-weight: 700; }

  .art { position: absolute; display: block; }
  .art--tree { background: radial-gradient(closest-side, var(--tree) 0%, var(--tree-deep) 75%, rgba(47,122,56,0) 100%); }
  .art--bare { background: radial-gradient(closest-side, rgba(63,130,70,.55) 0%, rgba(63,130,70,0) 100%); }
  .art--roots { background: radial-gradient(closest-side, var(--tree-deep) 0%, rgba(47,122,56,.4) 55%, rgba(47,122,56,0) 100%); }

  .acronym { position: absolute; text-align: center; font-family: "Oswald", sans-serif; font-weight: 600; color: var(--accent); line-height: 1; }
  .acronym-label { position: absolute; text-align: center; color: var(--label); font-weight: 500; letter-spacing: 0.5px; }
  .acronym-label span { border-left: 1.5px solid var(--label); border-right: 1.5px solid var(--label); padding: 2px 6px; }

  .point { position: absolute; }
  .point h3 { display: flex; align-items: center; gap: 6px; font-weight: 700; color: var(--ink); }
  .point ul { list-style: none; }
  .point li { color: var(--ink-soft); font-weight: 500; }
  .point li::before { content: ""; display: inline-block; width: 3px; height: 3px; border-radius: 50%;
    background: var(--tree-deep); box-shadow: 4px 0 0 var(--tree-deep); margin: 0 8px 2px 0; vertical-align: middle; }

  .panel--compare .point h3 { font-size: 12.5px; height: 16px; }
  .panel--compare .point li { font-size: 9.6px; line-height: 13.7px; }
  .panel--compare .point--kit { left: 26px; width: 250px; }
  .panel--compare .point--opm { left: 312px; width: 255px; }
  .panel--compare .point svg { width: 18px; height: 18px; }

  .column-rule { position: absolute; left: 285px; top: 410px; width: 0; height: 510px; border-left: 3px dotted var(--accent); }
  .scroll-hint { position: absolute; left: 549px; top: 402px; width: 12px; height: 16px; }

  .panel--solo .point { left: 0; width: 100%; text-align: center; }
  .panel--solo .point-icon { display: block; margin: 0 auto 6px; width: 22px; height: 22px; }
  .panel--solo .point h3 { justify-content: center; font-size: 14px; }
  .panel--solo .point li { font-size: 11.5px; line-height: 16.2px; }
</style>
</head>
<body>

<section class="panel panel--compare" aria-label="KIT compared with OPM">
  <div class="top-band" role="img" aria-label="Green patterned header band"></div>
  <header class="header">
    <div class="brand"><span class="brand-dot"></span><span class="brand-name">Clearwater<br>Investing</span></div>
    <p class="tagline">Putting Capital Back to Work</p>
  </header>
  <div class="header-notch"></div>

  <div class="why-title">
    <svg width="40" height="36" viewBox="0 0 40 36" fill="none" stroke="#2f7a38" stroke-width="2"><rect x="6" y="3" width="26" height="28" rx="2"/><path d="M11 10h16M11 15h16M11 20h16M11 25h10"/></svg>
    <h2>WHY CLEARWATER INVESTING?</h2>
  </div>
  <svg class="divider" style="top:244px" viewBox="0 0 40 12" fill="none" stroke="#2f7a38" stroke-width="1.5"><path d="M0 6h40"/><circle cx="20" cy="6" r="5"/></svg>
  <p class="why-copy">
    <strong>MBA students at Harborview Graduate Institute</strong> planted the seeds for Clearwater Investing in the Fall of 2011.<br>
    We shared a common goal of <span class="goal">"Making Business Work Better"</span>.<br>
    We each had very different experiences in our business careers and our personal lives. We shared our stories and learned from each other. A vision for a new category of investing began to emerge - community-based, relationship-based investing that we call <strong>Clearwater Investing</strong>
  </p>
  <svg class="divider" style="top:338px" viewBox="0 0 40 12" fill="none" stroke="#2f7a38" stroke-width="1.5"><path d="M0 6h40"/><circle cx="20" cy="6" r="5"/></svg>

  <svg class="scroll-hint" viewBox="0 0 12 16" fill="none" stroke="#3e9a47" stroke-width="1.5"><path d="M2 2l4 4 4-4M2 9l4 4 4-4"/></svg>
  <div class="column-rule"></div>

  <div class="art art--tree" style="left:66px;top:392px;width:70px;height:54px" role="img" aria-label="Leafy tree illustration"></div>
  <div class="acronym" style="left:40px;top:450px;width:122px;font-size:38px">KIT</div>
  <div class="acronym-label" style="left:20px;top:487px;width:162px;font-size:10.5px"><span>KEEP IT TANGIBLE</span></div>
  <div class="art art--roots" style="left:74px;top:508px;width:54px;height:34px" role="img" aria-label="Tree roots illustration"></div>

  <div class="point point--kit" style="top:557px">
    <h3><svg viewBox="0 0 18 18" fill="none" stroke="var(--icon)" stroke-width="1.4"><path d="M4 1h7l4 4v12H4z"/><path d="M7 8h5M7 11h5M7 14h3"/></svg>SIMPLE</h3>
    <ul><li>Simple Interest</li><li>Simple documents</li></ul>
  </div>
  <div class="point point--kit" style="top:628px">
    <h3><svg viewBox="0 0 18 18" fill="none" stroke="var(--icon)" stroke-width="1.4"><circle cx="9" cy="6" r="3.5"/><path d="M3 17c0-4 2.5-6 6-6s6 2 6 6"/></svg>DIY – DO IT YOURSELF</h3>
    <ul><li>Fund the world that you want to live in</li><li>You make your own decisions</li></ul>
  </div>
  <div class="point point--kit" style="top:697px">
    <h3><svg viewBox="0 0 18 18" fill="none" stroke="var(--icon)" stroke-width="1.4"><circle cx="6" cy="6" r="2.5"/><circle cx="12" cy="6" r="2.5"/><path d="M1 15c0-3 2-5 5-5s5 2 5 5M8 12c1-1.3 2.3-2 4-2 3 0 5 2 5 5"/></svg>PEOPLE</h3>
    <ul><li>Relationship based</li><li>Intuition</li><li>Caring and love</li></ul>
  </div>
  <div class="point point--kit" style="top:780px">
    <h3><svg viewBox="0 0 18 18" fill="none" stroke="var(--icon)" stroke-width="1.4"><path d="M9 17s-5-5.5-5-9a5 5 0 0 1 10 0c0 3.5-5 9-5 9z"/><circle cx="9" cy="8" r="1.8"/></svg>LOCAL</h3>
    <ul><li>Community and culture based</li><li>Neighborhood, town/city, county, state, country</li><li>Local operations of international companies</li></ul>
  </div>

  <div class="art art--bare" style="left:396px;top:398px;width:58px;height:50px" role="img" aria-label="Bare tree illustration"></div>
  <div class="acronym" style="left:364px;top:450px;width:122px;font-size:34px">OPM</div>
  <div class="acronym-label" style="left:330px;top:487px;width:190px;font-size:10.5px"><span>OTHER PEOPLE'S MONEY</span></div>
  <div class="art art--roots" style="left:398px;top:508px;width:54px;height:34px" role="img" aria-label="Tree roots illustration"></div>

  <div class="point point--opm" style="top:564px">
    <h3><svg viewBox="0 0 18 18" fill="none" stroke="var(--icon)" stroke-width="1.4"><path d="M4 1h7l4 4v12H4z"/><path d="M7 8h5M7 11h5M7 14h3"/></svg>COMPLEX</h3>
    <ul><li>SEC filings: 10Q, 10K, 8K, S8, CMO, CDO,</li><li>Hedge Funds, Junk Bonds, Leverage, Arbitrage</li><li>Proxy Statements, Earnings Calls</li><li>Complex legal documents – court system interprets</li></ul>
  </div>
  <div class="point point--opm" style="top:662px">
    <h3><svg viewBox="0 0 18 18" fill="none" stroke="var(--icon)" stroke-width="1.4"><circle cx="5" cy="5" r="3"/><circle cx="13" cy="5" r="3"/><circle cx="9" cy="13" r="3"/></svg>EXPERTS</h3>
    <ul><li>Attorneys, CPAs, CFAs, VPs, CFREs, CEOs, EVPs,</li><li>Must rely on "experts" to interpret complex documents and complex data</li><li>"Experts" decide for you</li></ul>
  </div>
  <div class="point point--opm" style="top:759px">
    <h3><svg viewBox="0 0 18 18" fill="none" stroke="var(--icon)" stroke-width="1.4"><rect x="1.5" y="1.5" width="15" height="15"/><path d="M5 13V9M9 13V5M13 13V7"/></svg>NUMBERS</h3>
    <ul><li>ROI, ROA, PEG Ratio, Alpha, Beta, Option Pricing</li><li>GAAP, EBIT, EBT, EPS, Free Cash Flow, Asset Turnover</li><li>Fundstar Style Box, Asset Allocation, Diversification</li><li>Big Data</li></ul>
  </div>
  <div class="point point--opm" style="top:860px">
    <h3><svg viewBox="0 0 18 18" fill="none" stroke="var(--icon)" stroke-width="1.4"><circle cx="9" cy="8" r="6.5"/><path d="M2.5 8h13M9 1.5c2.5 2.5 2.5 10.5 0 13M9 1.5c-2.5 2.5-2.5 10.5 0 13M5 17h8"/></svg>GLOBAL</h3>
    <ul><li>Global decisions – local needs ignored</li><li>Hierarchal structures</li><li>Shareholder returns</li></ul>
  </div>
</section>

<section class="panel panel--solo" aria-label="KIT on its own">
  <div class="top-band" role="img" aria-label="Green patterned header band"></div>
  <header class="header">
    <div class="brand"><span class="brand-dot"></span><span class="brand-name">Clearwater<br>Investing</span></div>
    <p class="tagline">Putting Capital Back to Work</p>
  </header>
  <div class="header-notch"></div>

  <div class="why-title">
    <svg width="40" height="36" viewBox="0 0 40 36" fill="none" stroke="#2f7a38" stroke-width="2"><rect x="6" y="3" width="26" height="28" rx="2"/><path d="M11 10h16M11 15h16M11 20h16M11 25h10"/></svg>
    <h2>WHY CLEARWATER INVESTING?</h2>
  </div>
  <svg class="divider" style="top:244px" viewBox="0 0 40 12" fill="none" stroke="#2f7a38" stroke-width="1.5"><path d="M0 6h40"/><circle cx="20" cy="6" r="5"/></svg>
  <p class="why-copy">
    <strong>MBA students at Harborview Graduate Institute</strong> planted the seeds for Clearwater Investing in the Fall of 2011.<br>
    We shared a common goal of <span class="goal">"Making Business Work Better"</span>.<br>
    We each had very different experiences in our business careers and our personal lives. We shared our stories and learned from each other. A vision for a new category of investing began to emerge - community-based, relationship-based investing that we call <strong>Clearwater Investing</strong>
  </p>
  <svg class="divider" style="top:338px" viewBox="0 0 40 12" fill="none" stroke="#2f7a38" stroke-width="1.5"><path d="M0 6h40"/><circle cx="20" cy="6" r="5"/></svg>

  <div class="art art--tree" style="left:236px;top:362px;width:100px;height:76px" role="img" aria-label="Leafy tree illustration"></div>
  <div class="acronym" style="left:186px;top:440px;width:200px;font-size:52px">KIT</div>
  <div class="acronym-label" style="left:176px;top:494px;width:220px;font-size:14px"><span>KEEP IT TANGIBLE</span></div>
  <div class="art art--roots" style="left:248px;top:524px;width:78px;height:56px" role="img" aria-label="Tree roots illustration"></div>

  <div class="point" style="top:588px">
    <svg class="point-icon" viewBox="0 0 18 18" fill="none" stroke="var(--icon)" stroke-width="1.3"><path d="M4 1h7l4 4v12H4z"/><path d="M7 8h5M7 11h5M7 14h3"/></svg>
    <h3>SIMPLE</h3>
    <ul><li>Simple Interest</li><li>Simple documents</li></ul>
  </div>
  <div class="point" style="top:682px">
    <svg class="point-icon" viewBox="0 0 18 18" fill="none" stroke="var(--icon)" stroke-width="1.3"><circle cx="9" cy="6" r="3.5"/><path d="M3 17c0-4 2.5-6 6-6s6 2 6 6"/></svg>
    <h3>DIY – DO IT YOURSELF</h3>
    <ul><li>Fund the world that you want to live in</li><li>You make your own decisions</li></ul>
  </div>
  <div class="point" style="top:782px">
    <svg class="point-icon" viewBox="0 0 18 18" fill="none" stroke="var(--icon)" stroke-width="1.3"><circle cx="6" cy="6" r="2.5"/><circle cx="12" cy="6" r="2.5"/><path d="M1 15c0-3 2-5 5-5s5 2 5 5M8 12c1-1.3 2.3-2 4-2 3 0 5 2 5 5"/></svg>
    <h3>PEOPLE</h3>
    <ul><li>Relationship based</li><li>Intuition</li><li>Caring and love</li></ul>
  </div>
  <div class="point" style="top:894px">
    <svg class="point-icon" viewBox="0 0 18 18" fill="none" stroke="var(--icon)" stroke-width="1.3"><path d="M9 17s-5-5.5-5-9a5 5 0 0 1 10 0c0 3.5-5 9-5 9z"/><circle cx="9" cy="8" r="1.8"/></svg>
    <h3>LOCAL</h3>
    <ul><li>Community and culture based</li><li>Neighborhood, town/city, county, state, country</li><li>Local operations of international companies</li></ul>
  </div>
</section>

</body>
</html>
```